Meridale Dental Business Card

Please design a professional but colorful looking business card. Our new logo is attached. The card also needs the following information:
For ALL Your Dental Needs
Curtis L. Hobbel, D.D.S.
918-555-0147
20463-C North Fernwick, Bixby, OK 74031
www.meridaledentalok.example

Industry/Entity Type

Business

Colors

Designer to choose colors to be used in the design.

```html
<!DOCTYPE html>
<html lang="en">
<head>
<meta charset="utf-8">
<title>Meridale Dental Business Card</title>
<link rel="stylesheet" href="https://fonts.googleapis.com/css2?family=Archivo:wght@400;800&family=Courgette&display=swap">
<style>
  :root {
    --page-bg: #d9d9d9;
    --card-bg: #f5f5f6;
    --panel-grey: #c5c5c6;
    --panel-edge: #a8a8a6;
    --ink: #2f3b42;
    --text: #1a1a1a;
    --brand-blue: #1b6fb8;
    --accent-pink: #e1268a;
    --icon-blue: #1f6db6;
    --icon-green: #6abf3f;
    --icon-orange: #e85a24;
    --icon-shadow: #a7a7a7;
  }
  * { margin: 0; padding: 0; box-sizing: border-box; }
  html, body { width: 1200px; height: 729px; overflow: hidden; }
  body { background: var(--page-bg); font-family: "Archivo", Arial, sans-serif; }
  .card {
    position: absolute; left: 50px; top: 46px; width: 1100px; height: 636px;
    background: var(--card-bg); border-radius: 28px; overflow: hidden;
  }
  .brand-panel { position: absolute; left: 0; top: 0; }
  .brand-name {
    position: absolute; left: 40px; top: 262px; width: 420px;
    text-align: center; color: var(--ink);
    font-weight: 800; font-size: 52px; line-height: 1.08; letter-spacing: 1px;
  }
  .doctor-name {
    position: absolute; right: 64px; top: 114px;
    font-weight: 800; font-size: 33px; letter-spacing: 1.5px; color: var(--ink);
    white-space: nowrap;
  }
  .doctor-name .degree { color: var(--brand-blue); }
  .tagline {
    position: absolute; right: 64px; top: 172px;
    font-family: "Courgette", cursive; font-size: 28px; color: var(--accent-pink);
    white-space: nowrap;
  }
  .contact {
    position: absolute; right: 150px; text-align: right;
    font-size: 27px; line-height: 1.5; color: var(--text); white-space: nowrap;
  }
  .contact.phone { top: 292px; }
  .contact.address { top: 355px; }
  .contact.web { top: 480px; }
  .icon { position: absolute; left: 974px; width: 68px; height: 68px; }
  .icon.phone { top: 278px; }
  .icon.address { top: 368px; }
  .icon.web { top: 467px; }
</style>
</head>
<body>
  <div class="card">
    <svg class="brand-panel" width="520" height="636" viewBox="0 0 520 636" aria-hidden="true">
      <circle cx="105" cy="318" r="395" fill="var(--panel-edge)"/>
      <circle cx="105" cy="318" r="389" fill="var(--panel-grey)"/>
    </svg>
    <div class="brand-name">MERIDALE<br>DENTAL</div>

    <div class="doctor-name">CURTIS L. HOBBEL, <span class="degree">D.D.S.</span></div>
    <div class="tagline">For ALL Your Dental Needs</div>

    <div class="contact phone">918-555-0147</div>
    <div class="contact address">20463-C North Fernwick,<br>Bixby, OK 74031</div>
    <div class="contact web">www.meridaledentalok.example</div>

    <svg class="icon phone" viewBox="0 0 68 68" aria-hidden="true">
      <rect x="0" y="8" width="60" height="60" rx="6" fill="var(--icon-shadow)"/>
      <rect x="6" y="0" width="62" height="62" rx="7" fill="var(--icon-blue)"/>
      <path d="M27 22c2-2 4-1 5 1l2 4c1 2 0 3-1 4l-2 2c2 4 5 7 9 9l2-2c1-1 2-2 4-1l4 2c2 1 3 3 1 5l-2 2c-3 3-9 1-15-5s-8-12-5-15z" fill="#fff"/>
    </svg>
    <svg class="icon address" viewBox="0 0 68 68" aria-hidden="true">
      <rect x="0" y="8" width="60" height="60" rx="6" fill="var(--icon-shadow)"/>
      <rect x="6" y="0" width="62" height="62" rx="7" fill="var(--icon-green)"/>
      <rect x="35" y="14" width="4" height="36" fill="#fff"/>
      <path d="M39 20h11l4 4-4 4H39z" fill="#fff"/>
      <path d="M35 30H24l-4 4 4 4h11z" fill="#fff"/>
    </svg>
    <svg class="icon web" viewBox="0 0 68 68" aria-hidden="true">
      <rect x="0" y="8" width="60" height="60" rx="6" fill="var(--icon-shadow)"/>
      <rect x="6" y="0" width="62" height="62" rx="7" fill="var(--icon-orange)"/>
      <circle cx="37" cy="31" r="15" fill="none" stroke="#fff" stroke-width="3.5"/>
      <path d="M28 22c4 1 6 4 4 7s2 5 5 5-1 6-4 9M42 18c-2 3 0 5 3 5s5 3 3 7" fill="none" stroke="#fff" stroke-width="3"/>
    </svg>
  </div>
</body>
</html>
```